Residential building / Apartments for sale landing page

I need a website / landing page design for my latest development project - a residential building with 70+ apartments for sale. I need the design in layers in Photoshop/Illustrator/InDesign format with all the icons/shapes/maps/graphic assets in vector format (svg, ai, eps) as much as possible.

I prefer white website and please consider the performance/coding experience. We're not making something suitable only for a design contest with fancy parallax effects and confusing animations. We're trying to create usable and clean UI with good UX.

The website will be custom coded, i.e. I'm not using WordPress.

I know that the existing 3D photos are not good but for now you can use them or replace them with some stock photos. I'm going to create new 3D photos soon.

Industry/Entity Type

Real Estate Development

Number of Pages Required

1 page

```html
<!DOCTYPE html>
<html lang="en">
<head>
<meta charset="utf-8">
<title>Verdant Heights — Apartments for Sale</title>
<link rel="stylesheet" href="https://fonts.googleapis.com/css2?family=Montserrat:wght@400;500;600;700;800&family=Open+Sans:wght@400;600&display=swap">
<style>
:root{
  --green:#7dc242;
  --green-dark:#65a52f;
  --ink:#222;
  --muted:#777;
  --light:#f4f4f4;
  --dark:#1f1f1f;
  --white:#fff;
}
*{box-sizing:border-box;margin:0;padding:0}
html,body{width:1200px;height:3744px;overflow:hidden}
body{font-family:"Open Sans",Arial,sans-serif;color:var(--ink);background:var(--white);position:relative}
h1,h2,h3,.nav,.btn,.brand{font-family:"Montserrat",Arial,sans-serif}

/* header */
.site-header{position:absolute;top:0;left:0;width:1200px;height:80px;z-index:5;background:rgba(20,20,20,.55)}
.brand{position:absolute;left:190px;top:26px;display:flex;align-items:center;gap:10px;color:var(--white);font-weight:800;font-size:17px;letter-spacing:1px}
.brand-mark{width:16px;height:16px;background:var(--green);border-radius:50%}
.topbar{position:absolute;right:190px;top:8px;font-size:11px;color:#ddd;display:flex;gap:14px}
.nav{position:absolute;right:190px;top:42px;display:flex;gap:30px;font-size:11px;font-weight:600;color:var(--white);letter-spacing:.5px}

/* hero */
.hero{position:absolute;top:0;left:0;width:1200px;height:600px;background:linear-gradient(100deg,#2b2f2c 0%,#4c5a4a 35%,#8fa08a 60%,#b7c0ba 80%,#6f7e72 100%)}
.hero-copy{position:absolute;left:190px;top:220px;width:520px;color:var(--white)}
.hero-copy h1{font-size:33px;line-height:1.25;font-weight:700}
.hero-copy .accent{color:var(--green)}
.btn{display:inline-block;background:var(--green);color:var(--white);font-size:12px;font-weight:700;padding:12px 26px;letter-spacing:.5px;margin-top:26px}
.scroll{position:absolute;left:565px;top:540px;width:70px;height:70px;border-radius:50%;background:var(--white);text-align:center;font-size:9px;font-weight:600;padding-top:38px;color:#444;z-index:3}
.scroll svg{position:absolute;left:29px;top:16px}

/* sections */
.section-title{text-align:center;font-size:31px;font-weight:700;letter-spacing:1px;color:var(--ink)}
.rule{width:60px;height:3px;background:var(--green);margin:14px auto 0}

.presentation{position:absolute;top:600px;left:0;width:1200px;height:480px}
.presentation .section-title{margin-top:50px}
.pres-gallery{position:absolute;left:192px;top:120px;width:816px;height:240px;display:flex;gap:4px}
.pres-gallery div{flex:1}
.pres-label{position:absolute;left:192px;top:280px;width:270px;height:80px;background:var(--green);color:var(--white);padding:18px 20px}
.pres-label h3{font-size:17px;font-weight:700}
.pres-label p{font-size:10px;margin-top:6px}

.facilities{position:absolute;top:1080px;left:0;width:1200px;height:660px;background:linear-gradient(180deg,#f3f3f3,#ececec)}
.facilities .section-title{margin-top:52px}
.fac-grid{position:absolute;left:192px;top:120px;width:816px;display:grid;grid-template-columns:repeat(3,1fr);gap:12px}
.fac-card{background:var(--white);height:228px;text-align:center;padding-top:36px}
.fac-card svg{display:block;margin:0 auto}
.fac-card h3{font-size:15px;font-weight:500;margin-top:18px}
.fac-card p{font-size:10px;color:var(--muted);width:170px;margin:10px auto 0;line-height:1.5}
.fac-card .more{display:block;margin-top:18px;font-size:9px;font-weight:700;color:var(--green-dark);font-family:"Montserrat",sans-serif}

.construction{position:absolute;top:1740px;left:0;width:1200px;height:580px;background:var(--green)}
.con-photo{position:absolute;left:190px;top:80px;width:340px;height:340px;border-radius:50%;background:linear-gradient(135deg,#d9d4cb,#9b8c7a);border:8px solid var(--white)}
.con-photo-small{position:absolute;left:150px;top:350px;width:120px;height:120px;border-radius:50%;background:linear-gradient(135deg,#fafafa,#c9c9c9);border:6px solid var(--white)}
.con-copy{position:absolute;left:580px;top:110px;width:420px;color:var(--white)}
.con-copy h2{font-size:40px;font-weight:800;line-height:1.05;letter-spacing:1px}
.con-copy ul{list-style:none;margin-top:34px;font-size:11px;line-height:1.6}
.con-copy li{margin-bottom:12px;padding-left:14px;position:relative}
.con-copy li::before{content:"";position:absolute;left:0;top:7px;width:5px;height:5px;background:var(--white);border-radius:50%}
.dots{display:flex;gap:6px;margin-top:20px}
.dots span{width:8px;height:8px;border-radius:50%;background:var(--white)}

.location-map{position:absolute;top:2320px;left:0;width:1200px;height:440px;background:linear-gradient(135deg,#eceae4,#dfe3e6 50%,#e8e6df)}

.gallery{position:absolute;top:2760px;left:0;width:1200px;height:580px}
.gallery .section-title{margin-top:82px}
.gallery .intro{width:640px;margin:22px auto 0;text-align:center;font-size:14px;line-height:1.6;color:#444}
.gal-row{position:absolute;left:192px;top:300px;width:816px;display:flex;gap:26px}
.gal-card{flex:1;background:var(--white);box-shadow:0 2px 10px rgba(0,0,0,.12);padding:10px 10px 0;height:192px}
.gal-card div{height:150px}
.gal-card p{text-align:center;font-size:12px;padding-top:8px}
.gal-card.active{background:var(--green);color:var(--white)}

.contact{position:absolute;top:3340px;left:0;width:1200px;height:340px;background:linear-gradient(180deg,#2a2a2a,#1c1c1c)}
.contact h2{position:absolute;left:192px;top:60px;color:var(--white);font-size:32px;font-weight:700}
.contact .rule{position:absolute;left:192px;top:110px;margin:0}
.contact-list{position:absolute;left:192px;top:140px;color:#ddd;font-size:12px;line-height:2.5;list-style:none}
.contact-map{position:absolute;left:680px;top:50px;width:328px;height:240px;background:linear-gradient(135deg,#4a4a4a,#333)}
.map-pop{position:absolute;left:96px;top:40px;background:var(--white);font-size:9px;padding:6px 10px;color:#333}
.map-pin{position:absolute;left:150px;top:92px}
.copyright{position:absolute;top:3680px;left:0;width:1200px;height:64px;background:#111;color:#aaa;font-size:11px;text-align:center;line-height:64px}
</style>
</head>
<body>

<section class="hero" role="img" aria-label="Rendering of the green residential building with planted balconies"></section>

<header class="site-header">
  <div class="brand"><span class="brand-mark"></span>VERDANT HEIGHTS</div>
  <div class="topbar"><span>Contact</span><span>EN English</span></div>
  <nav class="nav"><span>VERDANT HEIGHTS</span><span>THE PROJECT</span><span>APARTMENTS</span><span>LOCATION</span><span>GALLERY</span></nav>
</header>

<div class="hero-copy">
  <h1>Sale of apartments directly from the investor with <span class="accent">10% discount</span>*Price from XXX EUR/m2</h1>
  <span class="btn">BUY NOW</span>
</div>
<div class="scroll"><svg width="12" height="14" viewBox="0 0 12 14"><path d="M6 0v12M1 7l5 5 5-5" stroke="#444" stroke-width="1.5" fill="none"/></svg>SCROLL</div>

<section class="presentation">
  <h2 class="section-title">PROJECT PRESENTATION</h2>
  <div class="rule"></div>
  <div class="pres-gallery">
    <div role="img" aria-label="Bright living room interior" style="background:linear-gradient(135deg,#e9e6e0,#b9b2a6)"></div>
    <div role="img" aria-label="Dining area with pendant light" style="background:linear-gradient(135deg,#cbbfae,#6d5a48)"></div>
    <div role="img" aria-label="Lounge with brick wall" style="background:linear-gradient(135deg,#c9926b,#e8ddd0)"></div>
  </div>
  <div class="pres-label"><h3>Minimalistic Style Apartment</h3><p>2 bedrooms · 74 m² · view</p></div>
</section>

<section class="facilities">
  <h2 class="section-title">FACILITIES / BENEFITS</h2>
  <div class="rule"></div>
  <div class="fac-grid">
    <div class="fac-card"><svg width="36" height="36" viewBox="0 0 36 36"><circle cx="18" cy="14" r="11" fill="#333"/><rect x="16" y="22" width="4" height="12" fill="#333"/></svg><h3>Green areas and gardens</h3><p>We will help you to get the result you dreamed of</p><span class="more">READ MORE</span></div>
    <div class="fac-card"><svg width="36" height="36" viewBox="0 0 36 36"><rect x="2" y="2" width="32" height="32" rx="4" fill="#333"/><text x="18" y="26" text-anchor="middle" font-size="20" font-weight="700" fill="#fff" font-family="Montserrat,sans-serif">P</text></svg><h3>Parking spaces</h3><p>We will help you to get the result you dreamed of</p><span class="more">READ MORE</span></div>
    <div class="fac-card"><svg width="40" height="36" viewBox="0 0 40 36"><circle cx="9" cy="24" r="7" fill="none" stroke="#333" stroke-width="3"/><circle cx="31" cy="24" r="7" fill="none" stroke="#333" stroke-width="3"/><path d="M9 24l8-12h10l4 12M17 12l-3-5" stroke="#333" stroke-width="3" fill="none"/></svg><h3>Bicycle parking</h3><p>We will help you to get the result you dreamed of</p><span class="more">READ MORE</span></div>
    <div class="fac-card"><svg width="36" height="36" viewBox="0 0 36 36"><path d="M7 2h22L18 18 29 34H7L18 18z" fill="#333"/></svg><h3>Outside workout area</h3><p>We will help you to get the result you dreamed of</p><span class="more">READ MORE</span></div>
    <div class="fac-card"><svg width="36" height="36" viewBox="0 0 36 36"><rect x="2" y="2" width="32" height="32" rx="6" fill="none" stroke="#333" stroke-width="3"/><path d="M12 11a10 10 0 0 1 0 14M18 8a15 15 0 0 1 0 20M24 5a20 20 0 0 1 0 26" stroke="#333" stroke-width="2.5" fill="none"/></svg><h3>NFC controlled access</h3><p>We will help you to get the result you dreamed of</p><span class="more">READ MORE</span></div>
    <div class="fac-card"><svg width="36" height="36" viewBox="0 0 36 36"><circle cx="18" cy="6" r="4" fill="#333"/><path d="M18 11v12M6 16h24M18 23l-8 11M18 23l8 11" stroke="#333" stroke-width="3" fill="none"/></svg><h3>Outdoor Yoga area</h3><p>We will help you to get the result you dreamed of</p><span class="more">READ MORE</span></div>
  </div>
</section>

<section class="construction">
  <div class="con-photo" role="img" aria-label="Team reviewing building plans at a table"></div>
  <div class="con-photo-small" role="img" aria-label="Rolled construction drawings"></div>
  <div class="con-copy">
    <h2>CONSTRUCTION<br>FEATURES</h2>
    <ul>
      <li>Wooden windows – Insulated frames reducing heat loss in winter and keeping rooms cool in summer.</li>
      <li>Sound barrier walls – Acoustic layers between apartments for quiet, private living spaces.</li>
      <li>High ceilings – Tall ceilings bring more light and space into every room.</li>
    </ul>
    <div class="dots"><span></span><span></span><span></span><span></span></div>
  </div>
</section>

<section class="location-map" role="img" aria-label="Street map of the neighbourhood around the building"></section>

<section class="gallery">
  <h2 class="section-title">PHOTO GALLERY</h2>
  <div class="rule"></div>
  <p class="intro">The basic philosophy of our studio is to create individual, aesthetically stunning solutions for our customers by lightning-fast development of projects employing unique styles.</p>
  <div class="gal-row">
    <div class="gal-card"><div role="img" aria-label="Construction progress photo, April" style="background:linear-gradient(135deg,#e5e5e5,#8a8a8a)"></div><p>April 2021</p></div>
    <div class="gal-card active"><div role="img" aria-label="Construction progress photo, March" style="background:linear-gradient(135deg,#f2f2f2,#cfcfcf)"></div><p>March 2021</p></div>
    <div class="gal-card"><div role="img" aria-label="Construction progress photo, February" style="background:linear-gradient(135deg,#dde3e8,#a8b2ba)"></div><p>February 2021</p></div>
  </div>
</section>

<footer class="contact">
  <h2>GET IN TOUCH</h2>
  <div class="rule"></div>
  <ul class="contact-list">
    <li>27 Linden Avenue, Springfield</li>
    <li>hello@verdantheights.com</li>
    <li>+1 555 010 2233</li>
  </ul>
  <div class="contact-map" role="img" aria-label="Dark map showing the sales office location">
    <div class="map-pop">27 Linden Avenue<br>Directions</div>
    <svg class="map-pin" width="22" height="30" viewBox="0 0 22 30"><path d="M11 0a11 11 0 0 0-11 11c0 8 11 19 11 19s11-11 11-19A11 11 0 0 0 11 0z" fill="#e53935"/><circle cx="11" cy="11" r="4" fill="#fff"/></svg>
  </div>
</footer>
<div class="copyright">© 2021 Verdant Heights. All Rights Reserved</div>

</body>
</html>
```